Label

I need a label designed for a bottle of water. I like the lightning bolt and the blue. But I do not want it exactly like the Zinn-oop.

The label needs to be 9 inches by 2.5 inches.

Pebble Water: Sip the Pebble

```html
<!DOCTYPE html>
<html lang="en">
<head>
<meta charset="utf-8">
<title>Pebble Water – Bottle Label</title>
<link rel="stylesheet" href="https://fonts.googleapis.com/css2?family=Bree+Serif&family=Ubuntu:wght@400;500&display=swap">
<style>
  :root {
    --backdrop: #d9d9d9;
    --label-blue: #2a5c9e;
    --label-blue-light: #3a7ac4;
    --label-blue-deep: #234f8c;
    --ink-white: #ffffff;
    --rule-white: rgba(255, 255, 255, 0.85);
  }
  html, body {
    margin: 0;
    padding: 0;
    width: 1200px;
    height: 506px;
    overflow: hidden;
    background: var(--backdrop);
  }
  .canvas {
    position: relative;
    width: 1200px;
    height: 506px;
  }
  .label {
    position: absolute;
    left: 50px;
    top: 56px;
    width: 1100px;
    height: 394px;
    background:
      radial-gradient(ellipse 55% 65% at 52% 35%, var(--label-blue-light) 0%, transparent 70%),
      radial-gradient(ellipse 40% 50% at 95% 85%, var(--label-blue-light) 0%, transparent 70%),
      linear-gradient(180deg, var(--label-blue) 0%, var(--label-blue-deep) 100%);
    overflow: hidden;
  }
  .storm-art {
    position: absolute;
    left: 114px;
    top: 92px;
    width: 152px;
    height: 224px;
    border-radius: 6px;
    background: linear-gradient(180deg, rgba(255,255,255,0.28) 0%, rgba(255,255,255,0.12) 100%);
  }
  .brand-block {
    position: absolute;
    left: 290px;
    top: 120px;
    width: 694px;
    text-align: center;
    color: var(--ink-white);
  }
  .brand-name {
    margin: 0;
    font-family: "Bree Serif", Georgia, serif;
    font-weight: 400;
    font-size: 94px;
    line-height: 1;
    letter-spacing: 1px;
    white-space: nowrap;
  }
  .brand-rule {
    height: 1px;
    margin: 26px 0 8px;
    background: var(--rule-white);
    border: 0;
  }
  .tagline {
    margin: 0;
    font-family: "Ubuntu", Arial, sans-serif;
    font-weight: 400;
    font-size: 54px;
    line-height: 1.1;
    letter-spacing: 12px;
    white-space: nowrap;
  }
  .volume {
    position: absolute;
    left: 290px;
    top: 340px;
    width: 694px;
    margin: 0;
    text-align: center;
    color: var(--ink-white);
    font-family: "Ubuntu", Arial, sans-serif;
    font-weight: 500;
    font-size: 16px;
  }
</style>
</head>
<body>
  <div class="canvas">
    <section class="label">
      <div class="storm-art" role="img" aria-label="White line illustration of a cloud with a lightning bolt striking down"></div>
      <div class="brand-block">
        <h1 class="brand-name">Pebble Water</h1>
        <hr class="brand-rule">
        <p class="tagline">Sip the Pebble</p>
      </div>
      <p class="volume">1 Liter (33.8 fl. oz)</p>
    </section>
  </div>
</body>
</html>
```